DROPS LABELS

Hi again !
It's probably easiest I have you make the edits I need to our Labels.
If you want to design just 1 to begin, we can go off that for the rest. I need help the edits but also with laying the new info out
Overall, I'm happy with the front set up, I'm mostly focused on the L and R sides.
1.
Remove the Michigan symbol on the front - I'm thinking that will allow us to kinda center the big dosage in its space .
R SIDE : (I dont mind if it is sideways or the otherway, whichever looks best)
2.
Remove Barcode
Update the ingredients :
insert the word ORGANIC ahead of the last ingredient
(if it's a Full-Spectrum label, put a * ahead of *ORGANIC and add this below :
*Full-Spectrum CBD Hemp Extract contains trace amounts of THC no greater than 0.3%
under the Ingredients add the ALLERGEN
ALLERGEN : CONTAINS COCONUT
3.
Add the KWB warning (outlined):
These statements have not been approved by the KWB. This product is not intended to diagnose, treat, cure, or prevent any disease.
L SIDE :
I think I'll keep the descriptive paragraph but delete the suggested use

```html
<!DOCTYPE html>
<html lang="en">
<head>
<meta charset="utf-8">
<title>Brixa's Pure CBD Drops – Label</title>
<link rel="stylesheet" href="https://fonts.googleapis.com/css2?family=Archivo+Black&family=Roboto:wght@400;700&family=Roboto+Condensed:wght@300;400;700&display=swap">
<style>
  :root {
    --page: #eeeeee;
    --label: #ffffff;
    --ink: #1a1a1a;
    --ink-soft: #2b2b2b;
    --blue-deep: #14237a;
    --blue-mid: #2a4fc0;
    --red: #c7252f;
    --gold: #c9b27a;
    --rule: #222222;
  }
  * { box-sizing: border-box; margin: 0; padding: 0; }
  html, body { width: 1200px; height: 960px; overflow: hidden; }
  body {
    background: var(--page);
    font-family: "Roboto", sans-serif;
    color: var(--ink);
    display: flex;
    align-items: center;
    justify-content: center;
  }
  .label {
    width: 1140px;
    height: 520px;
    background: var(--label);
    display: grid;
    grid-template-columns: 380px 380px 380px;
    box-shadow: 0 2px 10px rgba(0,0,0,.08);
  }
  .panel { position: relative; padding: 40px 34px; overflow: hidden; }
  .panel + .panel { border-left: 1px dashed #dddddd; }

  /* Left side: description */
  .description {
    font-size: 15.5px;
    line-height: 26px;
    color: var(--ink-soft);
    text-align: justify;
  }
  .dosage-wrap { display: flex; gap: 10px; }
  .dosage-wrap .copy { flex: 1; text-align: left; }
  .dosage-chart {
    width: 130px;
    display: flex;
    gap: 8px;
    align-items: flex-end;
    flex-shrink: 0;
  }
  .dosage-list { list-style: none; font-size: 12px; line-height: 26px; padding-bottom: 44px; white-space: nowrap; }
  .dropper-art {
    width: 38px;
    height: 230px;
    flex-shrink: 0;
    background: linear-gradient(#f4f4f4, #d8d8d8);
    border-radius: 16px 16px 4px 4px;
  }
  .servings { font-size: 12px; font-weight: 700; margin-top: 4px; }

  /* Front */
  .front { padding: 44px 16px 30px; text-align: center; }
  .front-top { display: flex; align-items: center; justify-content: center; gap: 14px; }
  .leaf-art {
    width: 60px; height: 76px;
    flex-shrink: 0;
    background: radial-gradient(circle, #d9c48e, var(--gold));
    border-radius: 50% 50% 40% 40%;
  }
  .drops, .strength .cbd {
    font-family: "Archivo Black", sans-serif;
    line-height: 1;
    white-space: nowrap;
    background: linear-gradient(135deg, var(--blue-deep), var(--blue-mid) 55%, var(--blue-deep));
    -webkit-background-clip: text;
    background-clip: text;
    color: transparent;
  }
  .drops { font-size: 58px; }
  .brand {
    font-family: "Archivo Black", sans-serif;
    font-size: 58px;
    line-height: 1;
    color: var(--red);
    margin-top: 16px;
    white-space: nowrap;
  }
  .tagline {
    font-weight: 700;
    font-size: 22px;
    letter-spacing: 5px;
    margin-top: 14px;
    white-space: nowrap;
  }
  .strength { display: flex; align-items: center; justify-content: center; gap: 12px; margin-top: 12px; }
  .strength .mg {
    font-family: "Roboto Condensed", sans-serif;
    font-weight: 700;
    font-size: 36px;
    white-space: nowrap;
  }
  .strength .cbd { font-size: 78px; }
  .net {
    font-family: "Roboto Condensed", sans-serif;
    font-weight: 700;
    font-size: 16px;
    margin-top: 22px;
    white-space: nowrap;
  }

  /* Right side: ingredients */
  .facts {
    text-align: center;
    font-family: "Roboto Condensed", sans-serif;
    font-weight: 300;
  }
  .ingredients { font-size: 21px; line-height: 30px; }
  .allergen { font-size: 21px; line-height: 28px; margin-top: 26px; }
  .allergen strong { font-weight: 700; }
  .warning {
    border: 2px solid var(--rule);
    font-family: "Roboto", sans-serif;
    font-weight: 400;
    font-size: 14.5px;
    line-height: 22px;
    text-align: justify;
    padding: 12px;
    margin: 26px auto 0;
    width: 270px;
    color: var(--ink-soft);
  }
  .website { font-family: "Roboto", sans-serif; font-size: 18px; margin-top: 28px; }
  .origin { font-family: "Roboto", sans-serif; font-size: 13px; margin-top: 8px; }
</style>
</head>
<body>
  <main class="label">
    <section class="panel description">
      <p class="intro">BRIXA'S PURE CBD DROPS are simply impressive with just two essential ingredients making it the perfect natural solution for everyday use to improve both body and mind. PURE CBD is for the purist who prefers CBD and nothing else.</p>
      <div class="dosage-wrap">
        <p class="copy">The principal ingredient is a major component of the cannabis plant with inherent nature to work within the body and influence important functions to bring balance and a better sense of wellbeing for a good life.</p>
        <div class="dosage-chart">
          <ul class="dosage-list">
            <li>63 MG CBD</li>
            <li>48 MG CBD</li>
            <li>32 MG CBD</li>
            <li>16 MG CBD</li>
          </ul>
          <div class="dropper-art" role="img" aria-label="Line drawing of a dropper marked 1.0, .75, .50 and .25 mL"></div>
        </div>
      </div>
      <p class="servings">(64 full-dropper servings per bottle)</p>
    </section>

    <section class="panel front">
      <div class="front-top">
        <div class="leaf-art" role="img" aria-label="Gold hemp leaf illustration"></div>
        <span class="drops">DROPS</span>
      </div>
      <div class="brand">BRIXA'S</div>
      <div class="tagline">PRIME BALANCE</div>
      <div class="strength">
        <span class="mg">4000 MG</span>
        <span class="cbd">CBD</span>
      </div>
      <p class="net">4000 MG CBD per bottle ( 2.16 fl oz. (64 mL)</p>
    </section>

    <section class="panel facts">
      <p class="ingredients">INGREDIENTS: ORGANIC (MCT) COCONUT OIL, ORGANIC PURE CANNABIDIOL (CBD) CRYSTALLINE</p>
      <p class="allergen"><strong>ALLERGEN</strong> :<br>CONTAINS COCONUT</p>
      <p class="warning">These statements have not been approved by the KWB. This product is not intended to diagnose, treat, cure, or prevent any disease.</p>
      <p class="website">www.BRIXASCBD.com</p>
      <p class="origin">MADE IN MICHIGAN</p>
    </section>
  </main>
</body>
</html>
```